Lumetta small bites needs a website.

I have a small dessert bite catering business creating uniquely crafted small dessert bites made with high quality ingredients focusing on gluten free and vegan options.
I would like a website to show off my creations and provide a way for customers to reach me. I work out of a catering kitchen so would include the address of the kitchen as well as my phone number and email etc.

I already own the “www.lumettasmallbites.example” domain but have not used it yet. I have zero knowledge on website creation and design so need help in design as well as coding. I’m not sure how many pages I need designed. I would like one for the dessert bar / catering focus and one for my tasting boxes. I would like a way to upload new tasting box pictures and information to the website as they come out.

Target Market(s)

Individuals or businesses wanting to buy small bite desserts for weddings, gatherings and events for a dessert bar table. I also am creating monthly / seasonal tasting boxes (holiday, Valentine’s Day, etc) that I’d like to highlight.

Industry/Entity Type

Dessert catering, vegan and gluten free

Coding

Coded - Design and coding required

Number of Pages Required

2 page

Colors
E54698
E96AAD
F1A4CE
F9D9EA
FCEFF6

Requirements
Must have
• Pictures of my desserts and text explaining my process of creating individual flavor profiled desserts for people. I would like it to match the current color scheme and vibe of my logo. Must say that I am a catering company so don’t have a bakery but do have frozen tasting boxes available at the store front of the commercial kitchen that I use.
Nice to have
• I would like the website to have the vibe and colors of my logo but would welcome additional creativity from the designer. Include pink and brown as the main colors

```html
<!DOCTYPE html>
<html lang="en">
<head>
<meta charset="utf-8">
<title>Lumetta Small Bites</title>
<link rel="stylesheet" href="https://fonts.googleapis.com/css2?family=Playfair+Display:wght@600;700&family=Montserrat:wght@400;500;600&family=Poppins:wght@400;500;600&display=swap">
<style>
:root{
  --pink-hot:#E54698;
  --pink:#E96AAD;
  --pink-bright:#F47FDD;
  --pink-soft:#F1A4CE;
  --pink-pale:#F9D9EA;
  --blush:#FCEFF6;
  --brown:#5B2E12;
  --brown-deep:#50321F;
  --ink:#2a1a12;
  --white:#ffffff;
}
*{margin:0;padding:0;box-sizing:border-box}
html,body{width:734px;height:1200px;overflow:hidden;background:var(--blush)}
body{position:relative;font-family:'Montserrat',sans-serif;color:var(--ink)}

.hero{position:absolute;left:0;top:0;width:734px;height:500px}
.hero-bg{position:absolute;left:0;top:0}
.hero-title{position:absolute;left:0;top:190px;width:734px;text-align:center;color:var(--white);font-family:'Playfair Display',serif;font-weight:700;font-size:38px;line-height:44px;white-space:nowrap}
.hero-sub{position:absolute;left:0;top:247px;width:734px;text-align:center;color:var(--white);font-size:13px;line-height:20px;white-space:nowrap}
.btn{position:absolute;display:block;border-radius:12px;background:var(--pink-bright);color:var(--brown);font-weight:600;text-transform:uppercase;text-align:center;white-space:nowrap}
.hero-btn{left:303px;top:300px;width:128px;height:18px;line-height:18px;font-size:8.4px}

.nav{position:absolute;left:145px;top:21px;width:446px;height:25px;border-radius:13px;background:var(--pink-bright);font-size:7.4px;color:var(--ink)}
.nav-link{position:absolute;top:0;line-height:25px;white-space:nowrap;color:inherit;text-decoration:none}
.nav-contact{position:absolute;left:381px;top:4px;width:56px;height:17px;line-height:17px;text-align:center;background:var(--white);border-radius:9px;text-transform:uppercase;font-size:7.2px;color:var(--brown)}
.brand-badge{position:absolute;left:311px;top:0;width:111px;height:104px;background:var(--blush);border:2px solid var(--brown);border-top:none;border-radius:0 0 56px 56px;display:flex;flex-direction:column;align-items:center;justify-content:center;gap:6px;padding-top:6px}
.brand-badge .mark{width:30px;height:30px;border-radius:50%;background:var(--pink)}
.brand-name{font-family:'Playfair Display',serif;font-weight:700;color:var(--brown);font-size:19px;line-height:1}

.seal{position:absolute;left:337px;top:453px;width:60px;height:60px;border-radius:50%;background:var(--white);border:2px solid var(--brown);display:flex;align-items:center;justify-content:center}
.seal span{font-family:'Playfair Display',serif;font-weight:700;color:var(--brown);font-size:12px}

.about-photos{position:absolute;left:66px;top:545px;width:290px;height:185px;display:flex;gap:5px}
.about-photos div{flex:1}
.about-photos div:first-child{border-radius:6px 0 0 6px;background:linear-gradient(160deg,#8a8f9e,#d9d7de 45%,#b7a48c)}
.about-photos div:last-child{border-radius:0 6px 6px 0;background:linear-gradient(170deg,#c9a47f,#e4d7a8 50%,#b49c86)}
.about-title{position:absolute;left:380px;top:553px;font-family:'Playfair Display',serif;font-weight:700;color:var(--brown);font-size:27px;line-height:32px;white-space:nowrap}
.about-body{position:absolute;left:378px;top:585px;font-size:7.4px;line-height:10.1px;color:var(--ink);white-space:nowrap}
.about-body p+p{margin-top:10px}
.about-btn{left:378px;top:697px;width:95px;height:21px;line-height:21px;font-size:8.6px}

.gallery{position:absolute;left:0;top:772px;width:734px;height:236px;background:var(--pink-pale)}
.section-title{position:absolute;left:0;width:734px;text-align:center;font-family:'Playfair Display',serif;font-weight:600;color:var(--brown);font-size:16px;line-height:20px}
.gallery .section-title{top:23px}
.gallery-row{position:absolute;left:0;top:56px;width:734px;height:128px;display:flex;gap:6px}
.gallery-row div{flex:1}
.g1{background:linear-gradient(150deg,#5c7a3c,#f1ece6 45%,#c79a6a)}
.g2{background:linear-gradient(160deg,#8c8c88,#efe6c8 50%,#dcd2b0)}
.g3{background:linear-gradient(160deg,#9a9a98,#6e4236 50%,#e8e2dc)}
.g4{background:linear-gradient(160deg,#4b3a30,#8a5a36 55%,#5a3a22)}
.gallery-btn{position:absolute;left:330px;top:196px;width:73px;height:18px;border-radius:9px;background:var(--pink-hot);color:var(--white);font-family:'Poppins',sans-serif;font-weight:600;font-size:6px;line-height:18px;text-align:center}

.contact-section{position:absolute;left:0;top:1008px;width:734px;height:172px;font-family:'Poppins',sans-serif;color:var(--ink);text-align:center}
.contact-section .section-title{top:26px}
.contact-intro{position:absolute;left:0;top:52px;width:734px;font-size:6.2px;line-height:9.4px;white-space:nowrap}
.contact-list{position:absolute;left:0;top:81px;width:734px;font-size:6px;line-height:13.5px;white-space:nowrap}
.contact-list b{font-weight:600}
.contact-list a{color:var(--pink-hot);text-decoration:none}
.contact-list .addr{line-height:9px}

.footer{position:absolute;left:0;top:1180px;width:734px;height:20px;background:var(--brown-deep);color:var(--white);font-family:'Poppins',sans-serif;font-size:5.4px;text-align:center;line-height:20px}
</style>
</head>
<body>

<header class="hero">
  <svg class="hero-bg" width="734" height="500" viewBox="0 0 734 500">
    <defs>
      <linearGradient id="heroTone" x1="0" y1="0" x2="1" y2="1">
        <stop offset="0" stop-color="#3a2a22"/>
        <stop offset=".45" stop-color="#6b4226"/>
        <stop offset=".8" stop-color="#4a2c18"/>
        <stop offset="1" stop-color="#2b1d15"/>
      </linearGradient>
      <linearGradient id="edgeGlow" gradientUnits="userSpaceOnUse" x1="0" y1="0" x2="734" y2="0">
        <stop offset="0" stop-color="#F47FDD" stop-opacity="0"/>
        <stop offset=".12" stop-color="#F47FDD" stop-opacity="0"/>
        <stop offset=".32" stop-color="#F47FDD"/>
        <stop offset=".68" stop-color="#F47FDD"/>
        <stop offset=".88" stop-color="#F47FDD" stop-opacity="0"/>
        <stop offset="1" stop-color="#F47FDD" stop-opacity="0"/>
      </linearGradient>
    </defs>
    <path d="M0 0H734V382Q367 584 0 382Z" fill="url(#heroTone)" role="img" aria-label="Dessert bar table with cannoli, cupcakes and chocolate cups at an event"/>
    <path d="M0 382Q367 584 734 382" fill="none" stroke="url(#edgeGlow)" stroke-width="5"/>
  </svg>

  <nav class="nav">
    <a class="nav-link" style="left:16px">Home</a>
    <a class="nav-link" style="left:59px">Dessert Bar &amp; Catering</a>
    <a class="nav-link" style="left:291px">Tasting Boxes</a>
    <a class="nav-contact">Contact</a>
  </nav>

  <div class="brand-badge">
    <div class="mark"></div>
    <div class="brand-name">Lumetta</div>
  </div>

  <h1 class="hero-title">Uniquely Flavorful Bites</h1>
  <p class="hero-sub">Artisanal vegan &amp; gluten-free dessert bites crafted for<br>your celebrations and everyday indulgence.</p>
  <span class="btn hero-btn">Explore Tasting Boxes</span>
</header>

<div class="seal"><span>Lumetta</span></div>

<section class="about">
  <div class="about-photos">
    <div role="img" aria-label="Plated mini cheesecakes on blue patterned dishes"></div>
    <div role="img" aria-label="Trays of mini cheesecakes topped with cherries"></div>
  </div>
  <h2 class="about-title">About Lumetta</h2>
  <div class="about-body">
    <p>Lumetta Small Bites is a boutique dessert catering company rooted in the<br>belief that every celebration deserves food that delights all the senses. Our<br>founder specializes in crafting miniature treats that combine global flavors<br>with modern technique, using premium ingredients and offering vegan<br>and gluten-free options so everyone can enjoy.</p>
    <p>From weddings and corporate receptions to intimate dinners, Lumetta’s<br>signature bites are designed to be beautiful, flavorful and memorable. We<br>work closely with each client to understand their palette and create<br>bespoke menus that reflect their story.</p>
  </div>
  <span class="btn about-btn">Our Process</span>
</section>

<section class="gallery">
  <h2 class="section-title">Taste the Inspiration</h2>
  <div class="gallery-row">
    <div class="g1" role="img" aria-label="Platter of cannoli and cherry-topped mini cakes"></div>
    <div class="g2" role="img" aria-label="Lemon ginger cheesecake bites"></div>
    <div class="g3" role="img" aria-label="Raspberry opera cake squares"></div>
    <div class="g4" role="img" aria-label="Full dessert bar spread at an event"></div>
  </div>
  <span class="gallery-btn">View Full Gallery</span>
</section>

<section class="contact-section">
  <h2 class="section-title">Get In Touch</h2>
  <p class="contact-intro">Ready to create the dessert bar of your dreams or order a tasting box? Reach out and<br>let's talk about your event and your unique flavor inspirations.</p>
  <div class="contact-list">
    <div><b>Email:</b> <a>info@lumettasmallbites.example</a></div>
    <div><b>Phone:</b> <a>+92 300-555-0147</a></div>
    <div><b>Kitchen Address:</b></div>
    <div class="addr">Commercial Kitchen<br>Lahore, Punjab, Pakistan</div>
  </div>
</section>

<footer class="footer">© 2026 Lumetta Small Bites. All rights reserved.</footer>

</body>
</html>
```